I want a double sided flyer possibly with a picture of a lawn or grass.
Company name, phone number, email, and logo
Halvorsen Turf Management, (404)726-1853,Halvorsen_Turf@brevimail.com
Company services
Fertilization and weed control,Lawn and Landscape maintenance, mowing, pruning, aeration, landscape and Christmas lights,

```html
<!DOCTYPE html>
<html lang="en">
<head>
<meta charset="utf-8">
<title>Halvorsen Turf Management – Flyer</title>
<link rel="stylesheet" href="https://fonts.googleapis.com/css2?family=Oswald:wght@400;500;600&family=Open+Sans:wght@400;600;700&display=swap">
<style>
  :root {
    --bg: #e9e6e1;
    --grass-light: #8fd13a;
    --grass-mid: #5fae22;
    --grass-dark: #3d8a16;
    --brand-green: #1f7a3a;
    --brand-deep: #14552a;
    --white: #ffffff;
    --paper: #f7f8f6;
    --shade: #dfe3df;
  }
  * { margin: 0; padding: 0; box-sizing: border-box; }
  html, body { width: 1200px; height: 707px; overflow: hidden; background: var(--bg); }
  .canvas { position: relative; width: 1200px; height: 707px; }

  .page {
    position: absolute; top: 70px; width: 390px; height: 560px;
    box-shadow: 0 6px 18px rgba(0,0,0,.25); overflow: hidden;
  }

  /* Front */
  .front { left: 170px; }
  .front-photo {
    position: absolute; inset: 0;
    background: linear-gradient(180deg, var(--grass-mid) 0%, var(--grass-light) 45%, var(--grass-mid) 80%, var(--grass-dark) 100%);
  }
  .front-band {
    position: absolute; top: 0; bottom: 0; left: 95px; width: 205px;
    background: rgba(255,255,255,.14);
  }
  .front-brand {
    position: absolute; top: 120px; left: 0; right: 0; text-align: center;
    color: var(--white); font-family: "Oswald", sans-serif; font-weight: 500;
  }
  .brand-dot { width: 56px; height: 56px; border-radius: 50%; background: var(--white); margin: 0 auto 16px; }
  .brand-name { font-size: 40px; line-height: 1; letter-spacing: 1px; }
  .brand-sub { font-size: 17px; line-height: 1.3; }
  .front-contact {
    position: absolute; left: 95px; width: 205px; top: 430px; height: 70px;
    background: rgba(255,255,255,.18); color: var(--white); text-align: center; padding-top: 8px;
  }
  .front-phone { font-family: "Oswald", sans-serif; font-weight: 500; font-size: 25px; line-height: 1.1; }
  .front-email { font-family: "Open Sans", sans-serif; font-size: 11.5px; font-weight: 600; margin-top: 4px; }

  /* Back */
  .back { left: 640px; background: var(--paper); }
  .back-side-shade {
    position: absolute; top: 0; bottom: 0; left: 0; width: 150px;
    background: linear-gradient(90deg, var(--white) 0%, var(--white) 80%, var(--shade) 100%);
  }
  .services-tag { position: absolute; top: 18px; left: 14px; width: 96px; }
  .services-tag svg { display: block; }
  .services-tag span {
    position: absolute; top: 20px; left: 0; right: 0; text-align: center;
    color: var(--white); font-family: "Open Sans", sans-serif; font-weight: 700; font-size: 13px; line-height: 1.1;
  }
  .photo-column { position: absolute; top: 18px; left: 150px; width: 135px; }
  .service-photo { height: 75px; border-bottom: 2px solid var(--white); }
  .photo-spreader { background: linear-gradient(135deg, #7bbf3a, #2f6e1c); }
  .photo-garden { background: linear-gradient(135deg, #d98bb4, #5aa23a 55%, #3b7d1f); }
  .photo-mower { background: linear-gradient(135deg, #6cb536, #c23a2e 60%, #3e8a1c); }
  .photo-pruning { background: linear-gradient(135deg, #a8d36a, #3d6f2a 60%, #c33b2c); }
  .photo-aeration { background: linear-gradient(135deg, #7fbf45, #8a6a44 60%, #4f8b2c); }
  .photo-lights { background: linear-gradient(135deg, #3a2a14, #d09a2a 50%, #2f4f2a); }
  .service-list { position: absolute; top: 18px; left: 292px; width: 90px; list-style: none; }
  .service-list li {
    height: 77px; display: flex; align-items: center;
    color: var(--brand-green); font-family: "Open Sans", sans-serif; font-weight: 600; font-size: 11px; line-height: 1.25;
  }
  .back-brand {
    position: absolute; top: 385px; left: 14px; width: 130px;
    color: var(--brand-green); font-family: "Oswald", sans-serif; font-weight: 500; text-align: center;
  }
  .back-brand .brand-dot { width: 30px; height: 30px; background: var(--brand-green); margin-bottom: 6px; }
  .back-brand .brand-name { font-size: 21px; }
  .back-brand .brand-sub { font-size: 11px; }
  .back-footer { position: absolute; left: 0; bottom: 0; width: 390px; height: 90px; }
  .back-phone {
    position: absolute; left: 18px; bottom: 30px;
    color: var(--white); font-family: "Oswald", sans-serif; font-weight: 500; font-size: 26px;
  }
</style>
</head>
<body>
<main class="canvas">
  <section class="page front">
    <div class="front-photo" role="img" aria-label="Close-up photograph of lush green lawn grass"></div>
    <div class="front-band"></div>
    <div class="front-brand">
      <div class="brand-dot"></div>
      <div class="brand-name">HALVORSEN</div>
      <div class="brand-sub">Turf Management</div>
    </div>
    <div class="front-contact">
      <div class="front-phone">(404)726-1853</div>
      <div class="front-email">Halvorsen_Turf@brevimail.com</div>
    </div>
  </section>

  <section class="page back">
    <div class="back-side-shade"></div>
    <div class="services-tag">
      <svg width="96" height="80" viewBox="0 0 96 80">
        <rect x="0" y="0" width="96" height="8" fill="var(--brand-deep)"/>
        <polygon points="0,10 96,10 96,68 48,80 0,68" fill="var(--brand-green)"/>
      </svg>
      <span>COMPANY<br>SERVICES</span>
    </div>

    <div class="photo-column">
      <div class="service-photo photo-spreader" role="img" aria-label="Photo of a fertilizer spreader on a lawn"></div>
      <div class="service-photo photo-garden" role="img" aria-label="Photo of a landscaped garden bed with flowers"></div>
      <div class="service-photo photo-mower" role="img" aria-label="Photo of a red lawn mower cutting grass"></div>
      <div class="service-photo photo-pruning" role="img" aria-label="Photo of pruning shears trimming a plant"></div>
      <div class="service-photo photo-aeration" role="img" aria-label="Photo of soil plugs from lawn aeration"></div>
      <div class="service-photo photo-lights" role="img" aria-label="Photo of colourful Christmas lights"></div>
    </div>

    <ul class="service-list">
      <li>Fertilization and weed control</li>
      <li>Lawn and Landscape maintenance</li>
      <li>mowing</li>
      <li>pruning</li>
      <li>aeration</li>
      <li>landscape and Christmas lights</li>
    </ul>

    <div class="back-brand">
      <div class="brand-dot"></div>
      <div class="brand-name">HALVORSEN</div>
      <div class="brand-sub">Turf Management</div>
    </div>

    <svg class="back-footer" viewBox="0 0 390 90" preserveAspectRatio="none">
      <path d="M0,18 C120,2 230,20 390,44 L390,90 L0,90 Z" fill="var(--brand-deep)"/>
      <path d="M0,30 C140,14 250,36 390,52 L390,90 L0,90 Z" fill="var(--brand-green)"/>
      <path d="M150,70 C240,58 310,50 390,46" stroke="var(--white)" stroke-width="2" fill="none"/>
      <path d="M170,80 C250,68 320,60 390,56" stroke="var(--white)" stroke-width="1" fill="none"/>
    </svg>
    <div class="back-phone">(404)726-1853</div>
  </section>
</main>
</body>
</html>
```